Live Webcasting Host Wants Template/Theme to Jumpstare Ecommerce Site

Please,Please, Please READ ALL OF THE DESCRIPTION. Thank you.

I need a template for a look for my developer to work with in designing an ecommerce site where clients pay a monthly fee for streaming services and video on demand.

I'll need 2 pages designed:
1) public page
2) client log in landing page.

Please use a CMS (WP preferred) as this will allow is for further content to be added after delivery. Please include the pricing text in boxes in slides (pdf) to help fill out you design for the home page.

The attached slides are to give you a general layout of how I envision the pages. Yes I would like the Client page to be tabbed from the side like in the attached slide.

I've attached company logos for use along with the accompanying .psd and .ai files in the zip. Use the colors in logo in site design.

Thank you for your time.

Please, no designs. This is for a CMS for webpage design like WordPress or Joomla. Thanks. Added Friday, January 13, 2017

Target Market(s)

Churches, Organizations, Civic Organizations, Government Agencies (State, Local) -BUT don't let this deter your creativity. Decision makers/influencers will be video production and/or IT personnel.

Industry/Entity Type

It Company

Font styles to use
Sans Serif

Colors
f5f5f5
e8e8e8
333333
fece3e
cbcbcb
33a6d7
000000

Requirements
Must have
• Responsive Design
Nice to have
• One Page Design
Should not have
• SHOULD NOT HAVE White overall background but use white in other ways if you like.

```html
<!DOCTYPE html>
<html lang="en">
<head>
<meta charset="utf-8">
<title>Lumora</title>
<link href="https://fonts.googleapis.com/css2?family=Lato:wght@400;700&family=Oswald:wght@600;700&display=swap" rel="stylesheet">
<style>
:root{
  --yellow:#fece3e;
  --orange:#f7a21b;
  --ink:#000000;
  --text:#333333;
  --muted:#9a9a9a;
  --band:#e8e8e8;
  --soft:#f5f5f5;
  --line:#cbcbcb;
  --blue:#33a6d7;
  --red:#c4121a;
  --btn:#ffec1a;
}
*{box-sizing:border-box;margin:0;padding:0}
html,body{width:1104px;height:1200px;overflow:hidden;background:#fff;font-family:'Lato',sans-serif;color:var(--text)}
.page{position:relative;width:1104px;height:1200px}
.hero{position:absolute;left:0;top:0;width:1104px;height:593px;
  background:radial-gradient(ellipse at 50% 10%,#b9bfc8 0%,transparent 55%),
  linear-gradient(160deg,#8c8f94 0%,#6d6f71 35%,#5b5650 60%,#3e4248 100%)}
.brand{position:absolute;left:100px;top:0;width:258px;height:102px;background:var(--yellow);
  display:flex;align-items:center;justify-content:center}
.brand-name{font-family:'Lato',sans-serif;font-weight:700;font-size:42px;color:var(--ink);letter-spacing:1px;line-height:1}
.login{position:absolute;left:862px;top:19px;height:41px;width:132px;background:var(--ink);border-radius:21px;
  color:#fff;font-weight:700;font-size:19px;letter-spacing:1px;display:flex;align-items:center}
.login-icon{width:41px;height:41px;background:var(--orange);border-radius:6px;margin-right:10px;display:flex;align-items:center;justify-content:center}
.nav{position:absolute;top:80px;left:414px;display:flex;align-items:center}
.nav a{color:#fff;text-decoration:none;font-size:15px;margin-right:36px}
.nav .home{margin-right:28px;display:flex}
.plan{position:absolute;border-radius:10px;text-align:center;text-transform:uppercase;box-shadow:0 4px 10px rgba(0,0,0,.35);overflow:hidden}
.plan-title{position:absolute;left:0;right:0;font-family:'Oswald',sans-serif;font-weight:700;letter-spacing:5px;line-height:1}
.plan-price{position:absolute;right:0;font-family:'Oswald',sans-serif;font-weight:700;color:var(--red);background:var(--yellow);border-radius:22px 0 0 22px;display:flex;align-items:center;justify-content:center;letter-spacing:1px}
.plan-band{position:absolute;left:0;right:0}
.plan-text{position:absolute;left:0;right:0;font-size:13px;letter-spacing:1.3px;line-height:16px;color:#222}
.plan-btn{position:absolute;left:50%;transform:translateX(-50%);width:148px;height:35px;border-radius:18px;background:var(--btn);border:2px solid #e8a400;
  font-family:'Oswald',sans-serif;font-weight:700;font-size:20px;letter-spacing:2px;color:#111;text-transform:none;display:flex;align-items:center;justify-content:center}
.plan-small{left:131px;top:213px;width:259px;height:300px;background:linear-gradient(180deg,#86b52a,#a6cf2a 60%,#78b02a)}
.plan-medium{left:405px;top:186px;width:294px;height:352px;background:linear-gradient(180deg,#b89630,#d2ad34 50%,#c29a2a)}
.plan-large{left:713px;top:213px;width:260px;height:300px;background:linear-gradient(180deg,#2fb8bc,#4fd0d2 55%,#1eaab0)}
.stripe{background:rgba(255,255,255,.2)}
.hello{position:absolute;left:87px;top:660px;width:550px}
.hello h1{font-weight:400;font-size:38px;letter-spacing:3px;color:var(--yellow)}
.hello h2{font-weight:400;font-size:19px;letter-spacing:2px;color:var(--ink);margin-top:14px}
.hello h3{font-weight:400;font-size:16px;letter-spacing:1px;color:var(--ink);margin-top:30px;margin-left:-2px}
.hello p{font-family:Arial,sans-serif;font-size:12px;line-height:21px;color:var(--muted);margin-top:16px}
.testimonials{position:absolute;left:651px;top:658px;width:420px}
.testimonials h2{font-weight:400;font-size:38px;letter-spacing:4px;color:var(--ink)}
.reviews{display:flex;gap:0;margin-top:24px}
.review{width:194px;padding-right:14px}
.review-head{display:flex;gap:14px}
.avatar{width:56px;height:56px;border-radius:50%;flex:none;background:radial-gradient(circle at 50% 40%,#e9b48b,#8a5a3c)}
.review-name{font-size:16px;letter-spacing:1.5px;color:var(--ink);margin-top:-4px;white-space:nowrap}
.review-lead,.review p{font-family:Arial,sans-serif;font-size:12px;line-height:21px;color:var(--muted)}
.review p{margin-top:18px}
.newsletter{position:absolute;left:0;top:968px;width:1104px;height:108px;background:var(--soft)}
.news-label{position:absolute;left:178px;top:43px;display:flex;align-items:center;gap:12px;font-size:15px;letter-spacing:.5px;color:var(--text);white-space:nowrap}
.news-input{position:absolute;left:497px;top:32px;width:305px;height:41px;background:#fff;font-size:11px;color:#ccc;padding:0 3px;display:flex;align-items:center}
.news-btn{position:absolute;left:817px;top:31px;width:114px;height:42px;background:var(--orange);color:var(--text);font-size:16px;display:flex;align-items:center;justify-content:center}
.footer-brand{position:absolute;left:78px;top:1124px}
.footer-brand .brand-name{font-size:44px}
.legal{position:absolute;left:286px;top:1139px;font-size:17px;letter-spacing:.5px;color:var(--text)}
.social{position:absolute;left:872px;top:1134px;display:flex;gap:8px}
.social span{width:31px;height:31px;border-radius:50%;background:#2b2b2b;display:block}
.to-top{position:absolute;left:1027px;top:1162px;width:38px;height:38px;background:var(--orange);display:flex;align-items:center;justify-content:center}
</style>
</head>
<body>
<div class="page">
  <section class="hero" role="img" aria-label="Blurred photo of a broadcast mixing desk in a control room"></section>

  <div class="brand"><div class="brand-name">LUMORA</div></div>

  <div class="login">
    <span class="login-icon">
      <svg width="22" height="24" viewBox="0 0 22 24"><circle cx="11" cy="7" r="5.5" fill="#111"/><path d="M1 23c0-6 4.5-9 10-9s10 3 10 9z" fill="#111"/></svg>
    </span>LOGIN
  </div>

  <nav class="nav">
    <span class="home"><svg width="30" height="26" viewBox="0 0 30 26"><path d="M15 2 2 13h4v11h7v-7h4v7h7V13h4z" fill="#f7a21b"/></svg></span>
    <a>FEATURES</a><a>PRICING</a><a>ABOUT US</a><a>WEBCASTING 101</a><a>CONTACT</a>
  </nav>

  <article class="plan plan-small">
    <div class="plan-band stripe" style="top:27px;height:52px"></div>
    <div class="plan-title" style="top:32px;font-size:44px;color:#1f2a10">SMALL</div>
    <div class="plan-price" style="top:80px;width:80px;height:37px;font-size:25px">$49</div>
    <div class="plan-band stripe" style="top:117px;height:62px"></div>
    <div class="plan-text" style="top:126px">400 viewer hours<br>(50 viewers watching 2 hrs-<br>4 times per month)</div>
    <div class="plan-text" style="top:200px">100 GB/month of video<br>storage</div>
    <div class="plan-btn" style="top:246px">More Info</div>
  </article>

  <article class="plan plan-medium">
    <div class="plan-band stripe" style="top:30px;height:60px"></div>
    <div class="plan-title" style="top:36px;font-size:52px;color:#ffe93a">MEDIUM</div>
    <div class="plan-price" style="top:90px;width:102px;height:44px;font-size:28px">$399</div>
    <div class="plan-band stripe" style="top:148px;height:82px"></div>
    <div class="plan-text" style="top:165px">4000 viewer hours<br>(500 viewers watching 2 hrs-<br>4 times per month)</div>
    <div class="plan-text" style="top:250px">500 GB/month of video<br>storage</div>
    <div class="plan-btn" style="top:295px">More Info</div>
  </article>

  <article class="plan plan-large">
    <div class="plan-band stripe" style="top:27px;height:52px"></div>
    <div class="plan-title" style="top:32px;font-size:44px;color:#0e4f5c">LARGE</div>
    <div class="plan-price" style="top:80px;width:86px;height:37px;font-size:25px">$999</div>
    <div class="plan-band stripe" style="top:117px;height:62px"></div>
    <div class="plan-text" style="top:126px">400 viewer hours<br>(50 viewers watching 2 hrs-<br>4 times per month)</div>
    <div class="plan-text" style="top:200px">2000 GB/month of video<br>storage</div>
    <div class="plan-btn" style="top:246px">More Info</div>
  </article>

  <section class="hello">
    <h1>HELLO THERE!</h1>
    <h2>WELCOME LUMORA STREAM SIMPLE</h2>
    <h3>LOREM IPSUM DOLAR AMET, CON SECTRTUR ADIPISC ING ELIT</h3>
    <p>Mes cuml dia sed in lacus ut eniascet ipsu ingerto aliiqt es site amet eismod ictor uten ligulate ameti dapibu ticdute numtsen lusto dolor ltissim comes cuml dia sed inertio lacusueni ascet dolingert aliiqt sit amet. Eism com odictor ut ligulate cot ameti dapibu ipsam voluptatem. Nemo enim ipsam voluptatem voluptas sit asper natur aut odit aut fugit sed quia consequuntur magni dolores eos qui ratione.</p>
  </section>

  <section class="testimonials">
    <h2>TESTIMONIALS</h2>
    <div class="reviews">
      <div class="review">
        <div class="review-head">
          <div class="avatar" role="img" aria-label="Portrait photo of a smiling customer"></div>
          <div><div class="review-name">DARA WELLS</div><div class="review-lead">Lorem ipsum dolorsit amt consetes ctetur.</div></div>
        </div>
        <p>Lorem ipsum dolor sit amt consetu les ctet adipiscing elituis eros uti ligula lacinia quis opt euismod.</p>
      </div>
      <div class="review">
        <div class="review-head">
          <div class="avatar" role="img" aria-label="Portrait photo of a smiling customer"></div>
          <div><div class="review-name">DARA WELLS</div><div class="review-lead">Lorem ipsum dolorsit amt consetes ctetur.</div></div>
        </div>
        <p>Lorem ipsum dolor sit amt consetu les ctet adipiscing elituis eros uti ligula lacinia quis opt euismod.</p>
      </div>
    </div>
  </section>

  <section class="newsletter">
    <div class="news-label">
      <svg width="25" height="17" viewBox="0 0 25 17"><rect x="1" y="1" width="23" height="15" fill="none" stroke="#f7a21b" stroke-width="2"/><path d="M1 1l11.5 9L24 1" fill="none" stroke="#f7a21b" stroke-width="2"/></svg>
      SUBCRIBE TO OUR NEWSLETTER
    </div>
    <div class="news-input">YOUR EMAIL ADDRESS</div>
    <div class="news-btn">SUBCRIBE</div>
  </section>

  <footer>
    <div class="footer-brand"><div class="brand-name">LUMORA</div></div>
    <div class="legal">© 2017 | PRIVACY POLICY</div>
    <div class="social"><span></span><span></span><span></span><span></span></div>
    <div class="to-top"><svg width="16" height="10" viewBox="0 0 16 10"><path d="M1 9l7-7 7 7" fill="none" stroke="#fff" stroke-width="1.5"/></svg></div>
  </footer>
</div>
</body>
</html>
```